Security and Technology Website - Bold and Confident, Something Unexpected

Silver Heron Systems is launching its first website and we need a great design to bring our brand to life and generate DTC and B2B leads.

We have a good logo, but I am struggling with the creative vision to bring it all together. While our industry is Alarm Systems and Technology, we want to create a site that is more friendly and less 'typical' than your standard IT sites.

It Must:
1. Appeal to both men and women. The logo is a bit masculine, so the colors and icons must soften this.
2. Feel modern - we need to convey that we we use the latest technology.
3. Feel a bit high-end. We are not a budget solution.
4. Have a distinct iconography and photo treatment.
5. Feel layered - not just a series of stacked horizontal modules.

It Should Not:
1. Feel like your typical IT website.

Here are resources to get you started!
• Staging Site:
https://silver-heron-systems.examplestore.test/
Password: Pippa

•Brand Guide: https://www.sketchboardly.test/design/QWRtLmPOx4K/vBnm8Kq2-ZXyTrLp7hd-QE/edit?utm_content=QWRtLmPOx4K&utm_campaign=designshare&utm_medium=link2&utm_source=sharebutton

• Logo and Fonts and Photos: :https://files.cloudvaultia.test/folders/7KpWmQ3xNrT8yLbZ2vHcJ5dFg9sAeUoPi?usp=sharing

• Design Inspiration (don't feel limited by this): https://www.sketchboardly.test/design/HJkPqRvBn2s/m7TyUiOp4LkJhGfDsA2-ZX/edit?utm_content=HJkPqRvBn2s&utm_campaign=designshare&utm_medium=link2&utm_source=sharebutton

______________

The winner will be asked to provide design files and finished PNGs of the overall design file, backgrounds, photo treatments/frames, and icons.

The winner will likely be engaged for a phase 2 to build out a product page.

Industry/Entity Type

Alarm Systems, Home Theatres, and Commercial IT Networking

Number of Pages Required

1 page

Font styles to use
Sans Serif

Colors
0054AA
0677BA
7BADD7
CADEEF
E8F1F8
0094D4
00A9DD
6FCCEA
C7EBF8
E9F6FB
EB3D1F
EC4F4E
F09395
F8D3D4
FCEDEE

Requirements
Must have
• 1. Appeal to both men and women. The logo is a bit masculine, so the colors and icons must soften this. 2. Feel modern - we need to convey that we we use the latest technology. 3. Feel a bit high-end. We are not a budget solution. 4. Have a distinct iconography and photo treatment. 5. Feel layered - not just a series of stacked horizontal modules.
Should not have
• 1. Should not feel like just another IT website.

```html
<!DOCTYPE html>
<html lang="en">
<head>
<meta charset="utf-8">
<title>Silver Heron Systems — Home &amp; Business Security</title>
<link href="https://fonts.googleapis.com/css2?family=Russo+One&family=Archivo:wght@500;600;700;800&family=Arimo:wght@400;700&display=swap" rel="stylesheet">
<style>
:root{
  --navy:#22247b;
  --navy-deep:#1b1d6c;
  --blue:#1592e6;
  --sky:#00a9dd;
  --pale:#e3f0fa;
  --red:#eb3d1f;
  --ink:#1a1a1a;
  --grey:#444;
  --white:#fff;
  --line:#d8dde6;
}
*{box-sizing:border-box;margin:0;padding:0}
html,body{width:1200px;height:5222px;overflow:hidden}
body{position:relative;font-family:"Arimo",Arial,sans-serif;color:var(--ink);background:var(--white)}
.abs{position:absolute}
.display{font-family:"Russo One",sans-serif;letter-spacing:1px;text-transform:uppercase}
.label{font-family:"Archivo",sans-serif;font-weight:700;text-transform:uppercase}
.btn{position:absolute;background:var(--blue);color:#fff;font-family:"Arimo",sans-serif;font-weight:700;font-size:13px;display:flex;align-items:center;justify-content:center;border-radius:5px}
.photo{position:absolute}

/* top bar + nav */
.topbar{top:0;left:0;width:1200px;height:32px;background:#fff;font-size:11px;color:#333}
.topbar .item{top:9px;display:flex;align-items:center;gap:8px}
.dot-ico{width:16px;height:16px;border-radius:50%;background:var(--blue);display:inline-block}
.nav{top:32px;left:0;width:1200px;height:49px;background:#fff;border-top:1px solid #eee}
.nav a{position:absolute;top:16px;font-size:13.5px;color:#222;text-decoration:none}
.nav a.active{color:var(--blue);font-weight:700}
.brand-badge{top:32px;left:61px;width:122px;height:122px;border-radius:50%;background:#fff;box-shadow:0 2px 8px rgba(0,0,0,.25);z-index:5;display:flex;align-items:center;justify-content:center;text-align:center;font-family:"Archivo",sans-serif;font-weight:800;font-size:14px;color:var(--navy);line-height:1.15}

/* hero */
.hero{top:81px;left:0;width:1200px;height:472px;background:radial-gradient(ellipse at 60% 45%,#4fa9e6 0%,#1d5ea8 30%,#0c2a5e 65%,#06153a 100%);color:#fff}
.hero h1{left:63px;top:243px;font-size:32px;line-height:41px;font-weight:400}
.hero .tri{left:63px;top:334px;display:flex;gap:30px;font-family:"Archivo",sans-serif;font-weight:600;font-size:24px}
.hero .tri span{display:flex;align-items:center;gap:8px}
.hero p{left:63px;top:380px;width:480px;font-size:13px;line-height:16px}
.slider-dots{display:flex;gap:8px}
.slider-dots i{display:block;width:38px;height:4px;background:#fff;border-radius:2px}
.slider-dots i:first-child{background:var(--blue)}

/* why */
.why{top:553px;left:0;width:1200px;height:355px;background:var(--navy);color:#fff;text-align:center}
.why h2{top:622px;left:0;width:1200px;font-size:40px}
.why .sub{top:678px;left:0;width:1200px;font-size:13.5px}
.why .col{top:722px;width:220px;text-align:center}
.why .col svg{display:block;margin:0 auto 10px}
.why .col div{font-family:"Archivo",sans-serif;font-weight:600;font-size:18px;line-height:24px;text-transform:uppercase}

/* founder */
.founder h3{left:497px;top:1033px;width:640px;font-family:"Archivo",sans-serif;font-weight:800;font-size:17.5px;line-height:26px;text-transform:uppercase}
.founder p{left:497px;width:660px;font-size:13.5px;color:#222}

/* steps */
.steps{top:1370px;left:0;width:1200px;height:406px;background:linear-gradient(180deg,#0a1030 0%,#15215a 50%,#0b1236 100%);color:#fff}
.steps h2{left:67px;top:1453px;font-size:40px}
.step{top:1534px;height:156px;border:1.5px solid rgba(255,255,255,.5)}
.step .num{font-family:"Russo One",sans-serif;font-size:66px;color:var(--blue);line-height:1}
.step .ttl{font-family:"Archivo",sans-serif;font-weight:700;font-size:19px;text-transform:uppercase}

/* feature cards */
.feature{background:var(--navy);color:#fff;padding:56px 0 0 61px}
.feature::before{content:"";position:absolute;inset:12px;border:1.5px solid rgba(255,255,255,.45);pointer-events:none}
.feature h4{font-family:"Archivo",sans-serif;font-weight:700;font-size:18px;letter-spacing:.5px;text-transform:uppercase}
.feature p{margin-top:16px;width:440px;font-size:13.5px;line-height:17px}
.feature .icons{display:flex;gap:22px;margin-top:10px}
.feature .ic{text-align:center;font-size:13.5px;font-weight:700;width:auto}
.feature .ic svg{display:block;margin:0 auto 6px}
.feature .go{margin-top:12px;width:174px;height:30px;position:relative}

/* products */
.section-title{font-size:40px}
.prod{top:3199px;width:344px;height:292px;background:#fff;border:1.5px solid var(--line);text-align:center;box-shadow:0 2px 6px rgba(0,0,0,.08)}
.prod svg{margin-top:68px}
.prod .ttl{margin-top:22px;font-family:"Archivo",sans-serif;font-weight:700;font-size:18px;text-transform:uppercase}
.prod .buy{margin-top:22px;font-size:13px;color:var(--blue)}

/* newsletter */
.news{top:3584px;left:0;width:1200px;height:126px;background:var(--pale)}
.news-input{left:730px;top:3626px;width:405px;height:43px;background:#fff;border-radius:22px;border:1px solid #cfe0ef;font-size:13px;color:#777;padding:14px 0 0 20px}

/* reviews */
.review{top:3872px;width:332px;height:338px;background:#fff;border:1.5px solid var(--line);text-align:center;box-shadow:0 2px 6px rgba(0,0,0,.08)}
.review.dark{background:var(--navy);color:#fff}
.review .g{position:absolute;right:22px;top:18px;width:24px;height:24px;border-radius:50%;border:3px solid var(--blue)}
.review .avatar{width:70px;height:70px;border-radius:50%;margin:70px auto 0;background:linear-gradient(160deg,#d5a383,#8a4b3a)}
.review .name{margin-top:14px;font-family:"Archivo",sans-serif;font-weight:700;font-size:18px;text-transform:uppercase}
.review .stars{margin-top:6px;color:#f5b400;font-size:28px;letter-spacing:4px}
.review .txt{margin:10px auto 0;width:262px;font-size:13px;line-height:16px}
.review.dark .name{color:var(--sky)}
.review .more{margin-top:6px;font-size:13px;color:var(--sky)}

/* contact */
.contact{top:4273px;left:0;width:1200px;height:586px;background:radial-gradient(ellipse at 50% 30%,#27338f 0%,#1b2470 55%,#101650 100%);color:#fff}
.field{left:290px;width:618px;background:#fff;border-radius:8px;color:#888;font-size:13px;padding:18px 0 0 16px}

/* footer */
.footer{top:4859px;left:0;width:1200px;height:322px;background:var(--navy-deep);color:#fff}
.footer h5{font-family:"Russo One",sans-serif;font-weight:400;font-size:17px;color:var(--sky);letter-spacing:.5px}
.footer ul{list-style:none;font-size:13px;line-height:32px;margin-top:8px}
.contact-list div{display:flex;align-items:flex-start;gap:10px;font-size:13px;margin-bottom:14px;line-height:15px}
.bottom{top:5181px;left:0;width:1200px;height:41px;background:#fff;font-size:12.5px;color:#222}
</style>
</head>
<body>

<!-- top bar -->
<div class="abs topbar">
  <div class="abs item" style="left:63px"><span class="dot-ico"></span>615.555.0142</div>
  <div class="abs item" style="left:190px"><span class="dot-ico"></span>482 Summit Ridge Ave. Suite 2-210 Lakemont, TN 37990</div>
  <div class="abs item" style="left:1040px;gap:18px"><span class="dot-ico"></span><span class="dot-ico"></span><span class="dot-ico"></span></div>
</div>

<nav class="abs nav">
  <a class="active" style="left:374px">Home</a>
  <a style="left:438px">Electronic Security ⌄</a>
  <a style="left:590px">Audio + Video ⌄</a>
  <a style="left:716px">Networking + Communication ⌄</a>
  <a style="left:940px">Cabling ⌄</a>
  <span class="btn" style="left:1028px;top:8px;width:109px;height:33px">Contact Us</span>
</nav>
<div class="abs brand-badge">Silver Heron<br>Systems</div>

<!-- hero -->
<section class="abs hero" role="img" aria-label="Photo of a glowing blue server-room corridor">
  <h1 class="abs display" style="top:162px">One solution for total security<br>home &amp; business</h1>
  <div class="abs tri" style="top:253px">
    <span><svg width="18" height="20" viewBox="0 0 18 20"><path d="M9 1 L17 4 V10 C17 15 13 18 9 19 C5 18 1 15 1 10 V4 Z" fill="none" stroke="#fff" stroke-width="2"/></svg>Safer</span>
    <span><svg width="18" height="20" viewBox="0 0 18 20"><path d="M9 1 L17 4 V10 C17 15 13 18 9 19 C5 18 1 15 1 10 V4 Z" fill="none" stroke="#fff" stroke-width="2"/></svg>Smarter</span>
    <span><svg width="18" height="20" viewBox="0 0 18 20"><path d="M9 1 L17 4 V10 C17 15 13 18 9 19 C5 18 1 15 1 10 V4 Z" fill="none" stroke="#fff" stroke-width="2"/></svg>Faster</span>
  </div>
  <p class="abs" style="top:299px">Lorem ipsum dolor sit amet, consectetur adipiscing elit, sed do eiusmod tempor incididunt ut labore et dolore magna aliqua.</p>
  <span class="btn" style="left:63px;top:349px;width:174px;height:30px">Get a Free Quote</span>
  <div class="abs slider-dots" style="left:531px;top:448px"><i></i><i></i><i></i></div>
</section>

<!-- why choose us -->
<section class="abs why"></section>
<h2 class="abs display" style="top:620px;left:0;width:1200px;text-align:center;font-size:40px;color:#fff">Why choose us</h2>
<div class="abs" style="top:678px;left:0;width:1200px;text-align:center;font-size:13.5px;color:#fff">Lorem ipsum dolor sit amet, consectetur adipiscing elit, sed do eiusmod tempor incididunt ut labore et dolore magna aliqua.</div>
<div class="abs why-col" style="top:716px;left:127px;width:220px;text-align:center;color:#fff">
  <svg width="62" height="62" viewBox="0 0 62 62" fill="none" stroke="#1592e6" stroke-width="2.5"><rect x="17" y="17" width="28" height="28" rx="3"/><rect x="25" y="25" width="12" height="12"/><path d="M24 17V7M31 17V7M38 17V7M24 45v10M31 45v10M38 45v10M17 24H7M17 31H7M17 38H7M45 24h10M45 31h10M45 38h10"/></svg>
  <div class="label" style="margin-top:10px;font-weight:600;font-size:18px;line-height:24px">Advanced<br>technology</div>
</div>
<div class="abs" style="top:716px;left:385px;width:220px;text-align:center;color:#fff">
  <svg width="62" height="62" viewBox="0 0 62 62" fill="none" stroke="#1592e6" stroke-width="2.5"><path d="M10 52 L38 24 M34 14 a10 10 0 0 0 14 14 l6 -6 -5 -5 -4 4 -5 -5 4 -4 -5 -5 z"/><path d="M52 52 L24 24 M10 10 l8 4 4 8 -4 4 -8 -4 -4 -8 z"/></svg>
  <div class="label" style="margin-top:10px;font-weight:600;font-size:18px;line-height:24px">Professional<br>installation</div>
</div>
<div class="abs" style="top:716px;left:642px;width:220px;text-align:center;color:#fff">
  <svg width="62" height="62" viewBox="0 0 62 62" fill="none" stroke="#1592e6" stroke-width="2.5"><circle cx="31" cy="20" r="11"/><path d="M31 14v12M27 17h6a2 2 0 0 1 0 4h-4a2 2 0 0 0 0 4h6"/><path d="M8 42 l10 -6 h14 l12 -4 a3 3 0 0 1 3 5 l-15 10 h-18 l-6 4"/></svg>
  <div class="label" style="margin-top:10px;font-weight:600;font-size:18px;line-height:24px">Affordable<br>packages</div>
</div>
<div class="abs" style="top:716px;left:871px;width:220px;text-align:center;color:#fff">
  <svg width="62" height="62" viewBox="0 0 62 62" fill="none" stroke="#1592e6" stroke-width="2.5"><path d="M52 31 a21 21 0 1 1 -6 -15"/><path d="M47 8v9h-9"/><text x="31" y="36" text-anchor="middle" font-family="Archivo,sans-serif" font-weight="700" font-size="14" fill="#1592e6" stroke="none">24/7</text></svg>
  <div class="label" style="margin-top:10px;font-weight:600;font-size:18px;line-height:24px">24/7<br>support</div>
</div>

<!-- founder -->
<svg class="abs" style="left:0;top:916px" width="52" height="160" viewBox="0 0 52 160"><path d="M0 0 L52 30 L0 110 Z" fill="#22247b"/><path d="M0 40 L46 60 L0 160 Z" fill="#eb3d1f"/></svg>
<svg class="abs" style="left:1145px;top:1165px" width="55" height="165" viewBox="0 0 55 165"><path d="M55 0 L0 60 L55 80 Z" fill="#22247b"/><path d="M55 45 L8 80 L55 165 Z" fill="#eb3d1f"/></svg>
<svg class="abs" style="left:66px;top:968px" width="316" height="338" viewBox="0 0 316 338">
  <path d="M6 6 H310 V210 L158 332 L6 210 Z" fill="#eb3d1f"/>
  <path d="M14 14 H302 V206 L158 322 L14 206 Z" fill="#1592e6"/>
</svg>
<div class="photo" role="img" aria-label="Portrait of the company founder" style="left:86px;top:988px;width:276px;height:210px;background:linear-gradient(160deg,#d9dde3,#9aa3b1)"></div>
<svg class="abs" style="left:86px;top:1197px" width="276" height="100" viewBox="0 0 276 100"><path d="M0 0 H276 V8 L138 98 L0 8 Z" fill="#8f98a8"/></svg>
<svg class="abs" style="left:312px;top:1196px" width="86" height="86" viewBox="0 0 86 86"><circle cx="43" cy="43" r="41" fill="#fff"/><circle cx="43" cy="43" r="33" fill="#22247b"/><path d="M36 30 L56 43 L36 56 Z" fill="#1592e6"/></svg>
<div class="founder">
  <h3 class="abs">I founded Silver Heron Systems to bring together technology and honest, reliable service.</h3>
  <p class="abs" style="top:1098px">I'm proud to call Tennessee home and even prouder to help keep its homes and businesses secure.</p>
  <p class="abs" style="top:1126px">Whether it's protecting or elevating your space, my goal is to make technology work for you.</p>
  <p class="abs" style="top:1154px">Think of us as your friendly, neighborhood tech expert—here to safeguard what matters most.</p>
  <span class="btn" style="left:497px;top:1202px;width:237px;height:29px">Tell Us How We Can Help</span>
  <div class="abs" role="img" aria-label="Handwritten signature of Marcus Hale" style="left:790px;top:1192px;width:122px;height:48px;background:linear-gradient(90deg,rgba(34,36,123,.08),rgba(34,36,123,.18))"></div>
</div>

<!-- steps -->
<section class="abs steps" role="img" aria-label="Dark photo of illuminated network hardware"></section>
<h2 class="abs display" style="left:67px;top:1450px;font-size:40px;color:#fff">A safer home or business</h2>
<div class="abs step" style="left:69px;width:342px;background:var(--navy);color:#fff;padding:14px 0 0 40px">
  <div style="position:absolute;inset:7px;border:1.5px solid rgba(255,255,255,.5)"></div>
  <div class="num" style="font-size:44px;margin-top:6px">01</div>
  <div class="ttl" style="font-size:17px;margin-top:4px">Build an instant quote</div>
  <div style="font-size:13px;line-height:16px;margin-top:6px;width:260px">Our live-estimate builder will guide you through a few questions</div>
  <div style="font-size:13px;color:var(--sky);text-decoration:underline;margin-top:2px">Get Started</div>
</div>
<div class="abs step" style="left:421px;width:359px;color:#fff;padding:22px 0 0 48px">
  <div class="num">02</div>
  <div class="ttl" style="margin-top:22px;margin-left:-2px">Schedule installation</div>
</div>
<div class="abs step" style="left:780px;width:359px;color:#fff;padding:22px 0 0 80px">
  <div class="num">03</div>
  <div class="ttl" style="margin-top:22px">Stay secure 24/7</div>
</div>

<!-- layered features -->
<div class="photo" role="img" aria-label="Photo of a woman using a wall-mounted security keypad" style="left:97px;top:1838px;width:511px;height:400px;background:linear-gradient(120deg,#e7e2da,#c9b9a6 60%,#a9906f)"></div>
<div class="abs feature" style="left:543px;top:1907px;width:560px;height:331px">
  <h4>Affordable security</h4>
  <p>Lorem ipsum dolor sit amet, consectetur adipiscing elit, sed do eiusmod tempor incididunt ut labore et dolore magna aliqua.</p>
  <div class="icons">
    <div class="ic"><svg width="56" height="56" viewBox="0 0 56 56" fill="none" stroke="#fff" stroke-width="2"><path d="M4 4 H52 V34 L28 52 L4 34 Z" stroke="#7badd7"/><path d="M17 28 L28 18 L39 28 M20 26 V38 H36 V26 M25 38 V31 H31 V38"/></svg>Homes</div>
    <div class="ic"><svg width="56" height="56" viewBox="0 0 56 56" fill="none" stroke="#fff" stroke-width="2"><path d="M4 4 H52 V34 L28 52 L4 34 Z" stroke="#7badd7"/><path d="M17 38 V26 H24 V38 M24 38 V18 L38 14 V38 M14 38 H42 M28 22h6M28 28h6M28 33h6"/></svg>Businesses</div>
  </div>
  <span class="btn go">View Now</span>
</div>

<div class="photo" role="img" aria-label="Photo of a modern living room with a large projection screen" style="left:592px;top:2238px;width:511px;height:399px;background:linear-gradient(110deg,#3a3530,#8a7765 45%,#d9c6a6 80%,#f0d27a)"></div>
<div class="abs feature" style="left:95px;top:2305px;width:558px;height:326px">
  <h4>Enviable entertainment</h4>
  <p>Lorem ipsum dolor sit amet, consectetur adipiscing elit, sed do eiusmod tempor incididunt ut labore et dolor</p>
  <div class="icons">
    <div class="ic"><svg width="56" height="56" viewBox="0 0 56 56" fill="none" stroke="#fff" stroke-width="2"><path d="M4 4 H52 V34 L28 52 L4 34 Z" stroke="#7badd7"/><rect x="16" y="17" width="24" height="16"/><path d="M20 22h16M20 27h16M22 37h12"/></svg>Home Theatres</div>
    <div class="ic"><svg width="56" height="56" viewBox="0 0 56 56" fill="none" stroke="#fff" stroke-width="2"><path d="M4 4 H52 V34 L28 52 L4 34 Z" stroke="#7badd7"/><path d="M16 28 L28 17 L40 28 M19 25 V38 H37 V25"/><circle cx="28" cy="31" r="3"/></svg>Smart Homes</div>
    <div class="ic"><svg width="56" height="56" viewBox="0 0 56 56" fill="none" stroke="#fff" stroke-width="2"><path d="M4 4 H52 V34 L28 52 L4 34 Z" stroke="#7badd7"/><rect x="14" y="20" width="28" height="12" rx="2"/><circle cx="21" cy="26" r="2"/><circle cx="28" cy="26" r="2"/><circle cx="35" cy="26" r="2"/></svg>Whole Home A/V</div>
  </div>
  <span class="btn go">View Now</span>
</div>

<div class="photo" role="img" aria-label="Photo of a business team on a video conference call" style="left:95px;top:2637px;width:511px;height:400px;background:linear-gradient(120deg,#e5e3df,#b7b0a6 55%,#4a4440)"></div>
<div class="abs" style="left:543px;top:2704px;width:560px;height:333px;background:var(--navy)"></div>
<div class="abs feature" style="left:543px;top:2704px;width:560px;height:333px;background:transparent">
  <h4>Connected businesses</h4>
  <p>Lorem ipsum dolor sit amet, consectetur adipiscing elit, sed do eiusmod tempor incididunt ut labore et dolor</p>
  <div class="icons">
    <div class="ic" style="line-height:16px"><svg width="56" height="56" viewBox="0 0 56 56" fill="none" stroke="#fff" stroke-width="2"><path d="M4 4 H52 V34 L28 52 L4 34 Z" stroke="#7badd7"/><rect x="15" y="16" width="26" height="17"/><path d="M22 38 H34 M28 33 V38"/><circle cx="24" cy="24" r="3"/></svg>Conference<br>Systems</div>
    <div class="ic"><svg width="56" height="56" viewBox="0 0 56 56" fill="none" stroke="#fff" stroke-width="2"><path d="M4 4 H52 V34 L28 52 L4 34 Z" stroke="#7badd7"/><path d="M20 16 c-3 4 -1 10 5 16 c6 6 12 8 16 5 l-4 -6 -4 2 c-3 -2 -5 -4 -7 -7 l2 -4 z"/></svg>Phones</div>
    <div class="ic"><svg width="56" height="56" viewBox="0 0 56 56" fill="none" stroke="#fff" stroke-width="2.2"><path d="M4 4 H52 V34 L28 52 L4 34 Z" stroke="#7badd7"/><path d="M15 22 a18 18 0 0 1 26 0 M19 26 a12 12 0 0 1 18 0 M23 30 a6 6 0 0 1 10 0"/><circle cx="28" cy="34" r="1.5" fill="#fff"/></svg>WiFi</div>
  </div>
  <span class="btn go">View Now</span>
</div>

<!-- products -->
<h2 class="abs display section-title" style="left:63px;top:3098px">Connect + protect your world</h2>
<div class="abs" style="left:63px;top:3159px;font-size:13.5px">Protect your people, assets, and information from whatever comes.</div>
<div class="abs prod" style="left:61px">
  <svg width="90" height="80" viewBox="0 0 90 80" fill="none" stroke="#111" stroke-width="3"><rect x="18" y="4" width="54" height="10" rx="3"/><path d="M30 14 v14 a15 15 0 0 0 30 0 v-14"/><path d="M28 50 a24 24 0 0 0 34 0 M22 60 a32 32 0 0 0 46 0 M16 70 a40 40 0 0 0 58 0"/></svg>
  <div class="ttl">Entry &amp; motion sensors</div>
  <div class="buy">Buy Now →</div>
</div>
<div class="abs prod" style="left:428px;border:none;color:#fff" role="img" aria-label="Photo of a person at a front door with a video doorbell, in a navy tint">
  <div style="position:absolute;inset:0;background:linear-gradient(160deg,#4a4fa3,#2c2f86)"></div>
  <div style="position:relative">
    <svg width="90" height="80" viewBox="0 0 90 80" fill="none" stroke="#fff" stroke-width="3"><rect x="30" y="4" width="30" height="72" rx="15"/><circle cx="45" cy="24" r="7"/><circle cx="45" cy="52" r="6"/><path d="M20 18 a20 20 0 0 0 0 28 M70 18 a20 20 0 0 1 0 28"/></svg>
    <div class="ttl">Video doorbells</div>
    <div class="buy" style="color:#6fccea">Buy Now →</div>
  </div>
</div>
<div class="abs prod" style="left:795px">
  <svg width="90" height="80" viewBox="0 0 90 80" fill="none" stroke="#111" stroke-width="3"><rect x="10" y="4" width="70" height="12" rx="3"/><path d="M16 16 v18 a29 29 0 0 0 58 0 v-18"/><circle cx="45" cy="40" r="15"/><circle cx="45" cy="40" r="6"/></svg>
  <div class="ttl">Security cameras</div>
  <div class="buy">Buy Now →</div>
</div>
<div class="abs slider-dots" style="left:531px;top:3515px"><i style="background:var(--blue)"></i><i style="background:var(--navy)"></i><i style="background:var(--navy)"></i></div>

<!-- newsletter -->
<section class="abs news"></section>
<h2 class="abs display" style="left:63px;top:3614px;font-size:32px">Subscribe to our newsletter</h2>
<div class="abs" style="left:63px;top:3668px;font-size:13px">Security Tips, Special Offers, and More!</div>
<div class="abs news-input">Email Address</div>
<svg class="abs" style="left:1096px;top:3633px" width="30" height="30" viewBox="0 0 30 30"><circle cx="15" cy="15" r="15" fill="#1592e6"/><path d="M9 15h12M16 10l5 5-5 5" fill="none" stroke="#fff" stroke-width="2"/></svg>

<!-- reviews -->
<h2 class="abs display" style="left:0;top:3772px;width:1200px;text-align:center;font-size:40px">Customers reviews</h2>
<div class="abs" style="left:0;top:3835px;width:1200px;text-align:center;font-size:13.5px">The installation was quick and seamless. I feel so much safer at home now!</div>
<div class="abs review" style="left:63px">
  <span class="g"></span>
  <div class="avatar" role="img" aria-label="Customer profile photo" style="background:linear-gradient(160deg,#e35a4a,#a22b24)"></div>
  <div class="name">Nora Pellin</div>
  <div class="stars">★★★★★</div>
  <div class="txt">I wanted to upgrade my basic home theater but I didn't know who to trust. SHS analyzed my existing</div>
</div>
<div class="abs review dark" style="left:434px">
  <span class="g" style="border-color:#fff"></span>
  <div class="avatar" role="img" aria-label="Customer profile photo" style="margin-top:56px;background:linear-gradient(160deg,#f3e7dc,#c9a585)"></div>
  <div class="name">June T</div>
  <div class="stars">★★★★★</div>
  <div class="txt">Fantastic service!! Use d Brightwatch and Homelume in the past, and their customer service does not compare to Silver Heron</div>
  <div class="more">Read More →</div>
</div>
<div class="abs review" style="left:805px">
  <span class="g"></span>
  <div class="avatar" role="img" aria-label="Customer profile photo" style="background:linear-gradient(160deg,#eadcc3,#b49469)"></div>
  <div class="name">Owen</div>
  <div class="stars">★★★★★</div>
  <div class="txt">I couldn't be more impressed with the service we received for our condo's security system upgrade.</div>
</div>

<!-- contact -->
<section class="abs contact"></section>
<h2 class="abs display" style="left:0;top:4310px;width:1200px;text-align:center;font-size:40px;color:#fff">Contact us</h2>
<div class="abs" style="left:300px;top:4373px;width:600px;text-align:center;font-size:13px;line-height:16px;color:#fff">Whether you are looking for more information, product help, or just want to bounce an idea around – we would love to hear from you.</div>
<div class="abs field" style="top:4433px;height:53px">Name</div>
<div class="abs field" style="top:4506px;height:53px">Business E-Mail</div>
<div class="abs field" style="top:4579px;height:53px">Phone Number</div>
<div class="abs field" style="top:4650px;height:126px">Message</div>
<span class="btn" style="left:290px;top:4794px;width:618px;height:28px;border-radius:6px">Contact Us</span>

<!-- footer -->
<footer class="abs footer">
  <div class="abs" style="left:67px;top:60px;display:flex;align-items:center;gap:12px;font-family:'Archivo',sans-serif;font-weight:800;font-size:24px;line-height:1.1">
    <span style="width:30px;height:30px;background:#fff;display:inline-block"></span>Silver Heron<br>Systems
  </div>
  <div class="abs" style="left:63px;top:195px;width:320px;font-size:13px;line-height:16px">I'm proud to call Tennessee home and even prouder to help keep its homes and businesses secure.</div>
  <div class="abs" style="left:454px;top:34px">
    <h5>RESIDENTIAL</h5>
    <ul><li>Home Security</li><li>Smart Homes</li><li>Home Theatres + A/V</li><li>WiFi</li><li>Cabling</li></ul>
  </div>
  <div class="abs" style="left:675px;top:34px">
    <h5>COMMERCIAL</h5>
    <ul><li>Cabling</li><li>Audio Video</li><li>Communication</li><li>Electronic Security</li><li>Project Consulting</li><li>Academic &amp; Non-Profit</li></ul>
  </div>
  <div class="abs contact-list" style="left:902px;top:34px;width:260px">
    <h5 style="margin-bottom:16px">CONTACT INFO</h5>
    <div><span class="dot-ico" style="flex:none"></span>615.555.0142</div>
    <div><span class="dot-ico" style="flex:none"></span>www.silverheron.example</div>
    <div><span class="dot-ico" style="flex:none"></span>482 Summit Ridge Ave. Suite 2-210<br>Lakemont, TN 37990</div>
    <h5 style="margin-top:14px">GET IN TOUCH</h5>
    <div style="margin-top:14px;gap:14px"><span class="dot-ico" style="width:24px;height:24px"></span><span class="dot-ico" style="width:24px;height:24px"></span></div>
  </div>
</footer>
<div class="abs bottom">
  <div class="abs" style="left:63px;top:13px">©2024 Silver Heron Systems. All rights reserved.</div>
  <div class="abs" style="right:63px;top:13px">Site Terms | Privacy Policy</div>
</div>

</body>
</html>
```